Web Design Project for starting CCTV/Camera security installer/reseller

Hello,

An old class mate is starting his own little CCTV/Camera security business as a one-man-gang.

He asked me to do his website but unfortunatly my design skills are not worth looking at :) The coding is no problem.

So I'm here to request a design.

What he wants is a site that lists the products he might install which is based on a small tree structure. So see it as a shop overview/display but without the baskets & cashout options.

you can find a site structure scheme, logo, product images & data sheet pdf's at this filebarn address:

https://www.filebarn.example/sh/kx7pq2931rv4zt8/wnLpHsRa3u/Vizor-Guard

the site itself is http://www.vizor-guard.example but only has a splash screen until I have a design for it.

the logo is a bit out of proportions, not sure if you can make something good out of it :/

Most content is in Dutch, I'll see if I can translate the needed parts...
Updates

Dear designers,

I have some good new for you.

You are allowed to use only that chrome Vizor-Guard part of the logo,
which should make things a lot easier to fit into your design ideas.

Keep up the creativity!

Dear designers,

I uploaded a new logo to the filebarn space.

It's a png but unfortunately it's not transparent, I'm still waiting for that one
but you know how to erase it in photoshop.

Target Market(s)

people looking for a visual solution to protect their company/home

Industry/Entity Type

Security

Requirements
Must have
• an iconized way to browse/display a tree. (not the traditional folder/explorer style)

maybe first a page with buttons/icons showing level 1 the group types (IP cams, IP servers, Accessories)

level 2 product groups (dome cam, ptz cam etc)

level 3 the actual product + a link to a pdf datasheet (if any)

could be multipage or maybe in/on-page since the product list won't be that huge.

maybe some random product info left and/or right so that the content area is not massive since he has not much to type
;)

```html
<!DOCTYPE html>
<html lang="en">
<head>
<meta charset="utf-8">
<title>Vizor-Guard Camera Surveillance</title>
<link href="https://fonts.googleapis.com/css2?family=Bree+Serif&family=Open+Sans:ital,wght@0,400;0,600;1,400&display=swap" rel="stylesheet">
<style>
:root{
  --blue:#1a6fc9;
  --navy:#1b4a93;
  --nav-top:#2b86dc;
  --nav-bottom:#0f5cb8;
  --red:#c8101a;
  --grey-text:#7a7a7a;
  --body-text:#555;
  --dark:#222;
  --pale:#eeeeee;
  --line:#d8d8d8;
  --hero-text:#b9d3f3;
}
*{box-sizing:border-box;margin:0;padding:0}
html,body{width:903px;height:1200px;overflow:hidden;background:#fff}
body{position:relative;font-family:"Open Sans",Arial,sans-serif;color:var(--body-text)}
.abs{position:absolute}
.serif{font-family:"Bree Serif",Georgia,serif}

/* header */
.brand{left:105px;top:40px;display:flex;align-items:center;gap:8px}
.brand-mark{width:14px;height:14px;background:var(--navy)}
.brand-name{font-family:"Bree Serif",Georgia,serif;font-size:22px;color:var(--navy)}
.reach{left:614px;top:18px;font-size:11px;color:var(--grey-text);line-height:19px}
.reach .phone{color:var(--red);font-size:14px}
.reach .mail{color:var(--dark)}
.handset{left:562px;top:6px}
.main-nav{left:458px;top:81px;width:337px;height:29px;display:flex;border-radius:3px;overflow:hidden;
  background:linear-gradient(var(--nav-top),var(--nav-bottom))}
.main-nav a{color:#fff;text-decoration:none;font-size:11px;font-weight:600;display:flex;align-items:center;justify-content:center;border-right:1px solid #0a4c9c;height:100%}
.main-nav a:last-child{border-right:0}
.red-rule{left:0;top:115px;width:903px;height:6px;background:var(--red)}

/* hero */
.hero{left:0;top:121px;width:903px;height:275px;background:var(--navy)}
.hero-title{left:137px;top:150px;font-size:28px;color:#fff}
.hero-list{left:137px;top:206px;list-style:none}
.hero-list li{font-family:"Bree Serif",Georgia,serif;color:var(--hero-text);font-size:14px;height:25.5px;display:flex;align-items:center;gap:9px}
.hero-photo{left:560px;top:121px;width:236px;height:275px;background:linear-gradient(90deg,#1b4a93 0%,#8fa3bf 35%,#d8d2c4 70%,#bfb39c 100%)}
.slider-dots{left:137px;top:367px;display:flex;gap:3px}
.slider-dots span{width:31px;height:3px;background:#0f2f66}
.slider-dots span:first-child{background:#6aa6ea}

/* product cards */
.card{top:417px;width:211px;height:253px;border:1px solid #e3e3e3;box-shadow:inset 0 0 6px rgba(0,0,0,.13)}
.card-title{position:absolute;left:13px;top:11px;font-family:"Bree Serif",Georgia,serif;font-size:15px;color:var(--grey-text)}
.card-title b{font-weight:400;color:var(--blue)}
.card-rule{position:absolute;left:13px;top:37px;width:184px;height:2px;background:#bbb}
.card-photo{position:absolute;left:13px;top:42px;width:184px;height:111px;border:2px solid #e6e6e6}
.card-text{position:absolute;left:13px;top:159px;width:186px;font-size:9.5px;line-height:14px}
.read-more{position:absolute;right:13px;top:219px;width:66px;height:20px;background:#9c9c9c;color:#fff;font-size:8.5px;display:flex;align-items:center;justify-content:center;gap:5px}

/* welcome */
.section-title{font-family:"Bree Serif",Georgia,serif;font-size:15px;color:var(--grey-text)}
.section-title b{font-weight:400;color:var(--blue)}
.pill{left:105px;width:477px;height:20px;background:var(--pale);border-radius:5px;font-size:10px;font-style:italic;color:#555;display:flex;align-items:center;padding-left:10px;gap:6px}
.welcome-copy{left:105px;top:819px;width:480px;font-size:10px;line-height:15px}
.install-photo{left:604px;top:724px;width:191px;height:124px;background:linear-gradient(135deg,#c9c6b8,#6c7f96 55%,#1e2a44)}

/* footer */
.footer-rule{left:105px;top:899px;width:690px;height:1px;background:var(--line)}
.footer-split{left:492px;top:914px;width:1px;height:246px;background:var(--line)}
.contact-head{font-family:"Bree Serif",Georgia,serif;font-size:15px;color:var(--blue)}
.contact-line{font-size:10.5px;color:var(--dark);line-height:15.5px}
.copyright{left:184px;top:1086px;font-size:9px;color:var(--dark)}
.social{left:252px;top:1114px;display:flex;gap:4px}
.social span{width:19px;height:19px;border-radius:50%;background:#111}
.field{left:528px;width:267px;border:1px solid #ccc;font-family:"Bree Serif",Georgia,serif;font-size:9.5px;color:var(--dark);padding:3px 6px}
.send{left:528px;top:1140px;width:55px;height:21px;background:var(--navy);color:#fff;font-family:"Bree Serif",Georgia,serif;font-size:12px;display:flex;align-items:center;justify-content:center}
</style>
</head>
<body>

<header>
  <div class="abs brand"><span class="brand-mark"></span><span class="brand-name">Vizor-Guard</span></div>
  <svg class="abs handset" width="50" height="56" viewBox="0 0 50 56" aria-hidden="true">
    <path d="M8 4c-6 4-6 14-3 24s8 18 14 20l4-3-6-10-5 3c-3-5-4-11-4-16l5-1-1-12z" fill="#111"/>
    <path d="M19 48c6 6 14 6 18 0 3-4 8-4 10 0" stroke="#111" stroke-width="1.5" fill="none"/>
  </svg>
  <div class="abs reach">
    <div>Contact us on &nbsp;<span class="phone">32 470 55 21 08</span></div>
    <div>or email us <span class="mail">info@vizor-guard.example</span></div>
  </div>
  <nav class="abs main-nav">
    <a style="width:71px">HOME</a>
    <a style="width:65px">TIPS</a>
    <a style="width:112px">INSTALLATION</a>
    <a style="width:89px">CONTACT</a>
  </nav>
  <div class="abs red-rule"></div>
</header>

<section>
  <div class="abs hero"></div>
  <div class="abs hero-photo" role="img" aria-label="Photo of a white dome surveillance camera mounted on a wall bracket"></div>
  <h1 class="abs hero-title serif" style="font-weight:400">Vizor - Guard</h1>
  <ul class="abs hero-list">
    <li><svg width="12" height="12" viewBox="0 0 12 12"><rect x="1" y="2" width="9" height="9" fill="none" stroke="#b9d3f3"/><path d="M3 6l2 2 6-7" stroke="#fff" stroke-width="1.5" fill="none"/></svg>Phasellus non lacus felis, et pharetra nibh.</li>
    <li><svg width="12" height="12" viewBox="0 0 12 12"><rect x="1" y="2" width="9" height="9" fill="none" stroke="#b9d3f3"/><path d="M3 6l2 2 6-7" stroke="#fff" stroke-width="1.5" fill="none"/></svg>Donec interdum mi non turpis ultricies pharetra.</li>
    <li><svg width="12" height="12" viewBox="0 0 12 12"><rect x="1" y="2" width="9" height="9" fill="none" stroke="#b9d3f3"/><path d="M3 6l2 2 6-7" stroke="#fff" stroke-width="1.5" fill="none"/></svg>Donec a est non felis dignissim facilisis et quis purus.</li>
    <li><svg width="12" height="12" viewBox="0 0 12 12"><rect x="1" y="2" width="9" height="9" fill="none" stroke="#b9d3f3"/><path d="M3 6l2 2 6-7" stroke="#fff" stroke-width="1.5" fill="none"/></svg>Etiam tincidunt congue &nbsp;ultrices leo convallis sed.</li>
    <li><svg width="12" height="12" viewBox="0 0 12 12"><rect x="1" y="2" width="9" height="9" fill="none" stroke="#b9d3f3"/><path d="M3 6l2 2 6-7" stroke="#fff" stroke-width="1.5" fill="none"/></svg>Cras sit amet nisi quis ligula vehicula venenatis.</li>
  </ul>
  <div class="abs slider-dots"><span></span><span></span><span></span></div>
</section>

<section>
  <article class="abs card" style="left:105px">
    <h2 class="card-title" style="font-weight:400">IP <b>CAMS</b></h2>
    <div class="card-rule"></div>
    <div class="card-photo" role="img" aria-label="Two white IP dome cameras" style="background:radial-gradient(ellipse at center,#e9e9e9,#fff 70%)"></div>
    <p class="card-text">Contrary to popular belief, Lorem Ipsum is not simply random text. It has roots in a piece of &nbsp;45 BC, making it over 2000 years old.....</p>
    <div class="read-more">Read More <svg width="8" height="8" viewBox="0 0 8 8"><circle cx="4" cy="4" r="3.3" fill="none" stroke="#fff"/><path d="M3.3 2.5l1.5 1.5-1.5 1.5" stroke="#fff" fill="none"/></svg></div>
  </article>
  <article class="abs card" style="left:345px">
    <h2 class="card-title" style="font-weight:400">IP <b>SERVERS</b></h2>
    <div class="card-rule"></div>
    <div class="card-photo" role="img" aria-label="Row of black rack servers" style="background:linear-gradient(#fff 15%,#3a3a3a 35%,#1c1c1c 70%,#eee 95%)"></div>
    <p class="card-text">Contrary to popular belief, Lorem Ipsum is not simply random text. It has roots in a piece of &nbsp;45 BC, making it over 2000 years old.....</p>
    <div class="read-more">Read More <svg width="8" height="8" viewBox="0 0 8 8"><circle cx="4" cy="4" r="3.3" fill="none" stroke="#fff"/><path d="M3.3 2.5l1.5 1.5-1.5 1.5" stroke="#fff" fill="none"/></svg></div>
  </article>
  <article class="abs card" style="left:584px">
    <h2 class="card-title" style="font-weight:400">IP <b>ACCESSORIES</b></h2>
    <div class="card-rule"></div>
    <div class="card-photo" role="img" aria-label="White USB cable and adapter accessories" style="background:radial-gradient(ellipse at center,#dcdcdc,#f4f4f4 70%)"></div>
    <p class="card-text">Contrary to popular belief, Lorem Ipsum is not simply random text. It has roots in a piece of &nbsp;45 BC, making it over 2000 years old.....</p>
    <div class="read-more">Read More <svg width="8" height="8" viewBox="0 0 8 8"><circle cx="4" cy="4" r="3.3" fill="none" stroke="#fff"/><path d="M3.3 2.5l1.5 1.5-1.5 1.5" stroke="#fff" fill="none"/></svg></div>
  </article>
</section>

<section>
  <h2 class="abs section-title" style="left:105px;top:699px;font-weight:400">WELCOME AT <b>VIZOR-GUARD CAMERA SURVEILANCE</b></h2>
  <div class="abs pill" style="top:729px"><span>»</span>Are you looking for a camera system for your home or company?</div>
  <div class="abs pill" style="top:757px"><span>»</span>Then you are at Vizor-Guard at the right address!</div>
  <div class="abs pill" style="top:785px"><span>»</span>We offer a large amount of surveilance camera’s, video storage systems and surveilance monitors.</div>
  <p class="abs welcome-copy">But we also have complete camera surveillance sets for you (analogue or IP camera’s) including the cables and power supplies, so that you don’t have to worry about additional components when ordering.</p>

  <h2 class="abs section-title" style="left:604px;top:699px;font-weight:400">INSTALLATION <b>SERVICE</b></h2>
  <div class="abs install-photo" role="img" aria-label="Technician in a blue hard hat installing a surveillance camera"></div>
</section>

<footer>
  <div class="abs footer-rule"></div>
  <div class="abs footer-split"></div>

  <h2 class="abs contact-head" style="left:107px;top:922px;font-weight:400">CONTACT</h2>
  <svg class="abs" style="left:105px;top:958px" width="9" height="12" viewBox="0 0 9 12"><path d="M4.5 0a4 4 0 0 0-4 4c0 3 4 8 4 8s4-5 4-8a4 4 0 0 0-4-4z" fill="#111"/><circle cx="4.5" cy="4" r="1.4" fill="#fff"/></svg>
  <div class="abs contact-line" style="left:121px;top:956px">Vizor Guard Camerabewaking<br>Lindenhofstraat 12,<br>9250 Waasberg,<br>Belgie</div>
  <svg class="abs" style="left:330px;top:960px" width="12" height="9" viewBox="0 0 12 9"><rect width="12" height="9" fill="#111"/><path d="M0 0l6 5 6-5" stroke="#fff" fill="none"/></svg>
  <div class="abs contact-line" style="left:346px;top:957px">info@vizor-guard.example</div>
  <svg class="abs" style="left:330px;top:982px" width="12" height="12" viewBox="0 0 12 12"><path d="M2 1l2.5 0 1 3-1.5 1c.7 1.5 1.8 2.6 3 3l1-1.5 3 1V10c0 .6-.5 1-1 1C5 11 1 7 1 2c0-.5.5-1 1-1z" fill="#111"/></svg>
  <div class="abs contact-line" style="left:346px;top:981px">+32 470 55 21 08</div>

  <p class="abs copyright">Copyright © 2012 Vizor-Guard. All Rights Reserved.</p>
  <div class="abs social" aria-label="Social links"><span></span><span></span><span></span></div>

  <h2 class="abs contact-head" style="left:528px;top:922px;font-weight:400">CONTACT FORM</h2>
  <div class="abs field" style="top:954px;height:20px">Name</div>
  <div class="abs field" style="top:984px;height:20px">Email</div>
  <div class="abs field" style="top:1015px;height:20px">Subject</div>
  <div class="abs field" style="top:1045px;height:83px">Questions &amp; Remarks</div>
  <div class="abs send">SEND</div>
</footer>

</body>
</html>
```